Halvercott Orthodontics business card

Using our existing logo (created with ArtFolio), please create a tasteful, contemporary business card. We are father and daughter orthodontists specializing in braces, clarafit, etc to design healthy, beautiful smiles for children, adolescents, and adults. We would like the design to be family-friendly but not childish.
The final design should include all of the information without looking cluttered (I hope! If necessary to achieve an optimal design, please consider making the card double-sided)
Purple, black, silver on a white card
Please include the following information:
Halvercott Orthodontics (logo)
Marguerite L. Halvercott, DMD
Douglas R. Halvercott, DMD

312 Bramblewood Street
North Andover, MA 01899
978.555.0142

847C Quarry Hollow Street
Methuen, MA 01898
978.555.0187

email frontdesk@halvercottortho.example
website www.halvercottortho.example

```html
<!DOCTYPE html>
<html lang="en">
<head>
<meta charset="utf-8">
<title>Halvercott Orthodontics business card</title>
<link href="https://fonts.googleapis.com/css2?family=Montserrat:wght@400;500;700&display=swap" rel="stylesheet">
<style>
  :root {
    --purple: #5e2b8e;
    --purple-deep: #52257e;
    --purple-text: #6a2fa0;
    --ink: #1e1e24;
    --card-white: #ffffff;
    --backdrop: #e9e6e2;
  }
  * { box-sizing: border-box; margin: 0; padding: 0; }
  html, body { width: 1200px; height: 931px; overflow: hidden; }
  body {
    background: var(--backdrop);
    font-family: "Montserrat", sans-serif;
    display: flex;
    flex-direction: column;
    align-items: center;
    justify-content: center;
    gap: 36px;
  }
  .card {
    width: 700px;
    height: 400px;
    border-radius: 22px;
    position: relative;
    overflow: hidden;
    box-shadow: 0 8px 24px rgba(0,0,0,0.18);
  }
  .card-back { background: var(--purple); }
  .card-back .wordmark {
    position: absolute;
    left: 0; right: 0; top: 50%;
    transform: translateY(-50%);
    text-align: center;
    color: var(--purple-deep);
    font-weight: 500;
    font-size: 44px;
    letter-spacing: 2px;
  }
  .card-front { background: var(--card-white); }
  .card-front .wordmark {
    position: absolute;
    right: 50px;
    top: 42px;
    color: var(--purple-text);
    font-weight: 500;
    font-size: 34px;
    letter-spacing: 1px;
  }
  .doctors {
    position: absolute;
    left: 50px;
    top: 122px;
  }
  .doctor-name {
    color: var(--purple-text);
    font-weight: 700;
    font-size: 22px;
    line-height: 1.2;
  }
  .doctor-role {
    color: var(--ink);
    font-size: 14px;
    margin: 2px 0 8px;
  }
  .divider {
    position: absolute;
    left: 50px;
    right: 50px;
    top: 228px;
    height: 2px;
    background: var(--purple);
  }
  .offices {
    position: absolute;
    left: 50px;
    right: 50px;
    top: 248px;
    display: flex;
    gap: 60px;
  }
  .office {
    font-style: normal;
    color: var(--ink);
    font-size: 14px;
    line-height: 1.5;
  }
  .office-phone {
    display: flex;
    align-items: center;
    gap: 8px;
    margin-top: 2px;
  }
  .contact-list {
    position: absolute;
    left: 50px;
    right: 50px;
    bottom: 34px;
    list-style: none;
    display: flex;
    gap: 36px;
    color: var(--ink);
    font-size: 14px;
  }
  .contact-list li {
    display: flex;
    align-items: center;
    gap: 8px;
  }
  .icon { width: 14px; height: 14px; fill: var(--purple-text); flex: none; }
</style>
</head>
<body>
  <section class="card card-back" aria-label="Card back">
    <div class="wordmark">Halvercott Orthodontics</div>
  </section>

  <section class="card card-front" aria-label="Card front">
    <div class="wordmark">Halvercott Orthodontics</div>

    <div class="doctors">
      <div class="doctor-name">Marguerite L. Halvercott, DMD</div>
      <div class="doctor-role">Managing Director</div>
      <div class="doctor-name">Douglas R. Halvercott, DMD</div>
    </div>

    <div class="divider"></div>

    <div class="offices">
      <address class="office">
        312 Bramblewood Street<br>
        North Andover, MA 01899
        <span class="office-phone">
          <svg class="icon" viewBox="0 0 24 24" aria-hidden="true"><path d="M6.6 10.8a15.1 15.1 0 0 0 6.6 6.6l2.2-2.2a1 1 0 0 1 1-.25 11.4 11.4 0 0 0 3.6.57 1 1 0 0 1 1 1V20a1 1 0 0 1-1 1A17 17 0 0 1 3 4a1 1 0 0 1 1-1h3.5a1 1 0 0 1 1 1c0 1.25.2 2.45.57 3.57a1 1 0 0 1-.25 1z"/></svg>
          978.555.0142
        </span>
      </address>
      <address class="office">
        847C Quarry Hollow Street<br>
        Methuen, MA 01898
        <span class="office-phone">
          <svg class="icon" viewBox="0 0 24 24" aria-hidden="true"><path d="M6.6 10.8a15.1 15.1 0 0 0 6.6 6.6l2.2-2.2a1 1 0 0 1 1-.25 11.4 11.4 0 0 0 3.6.57 1 1 0 0 1 1 1V20a1 1 0 0 1-1 1A17 17 0 0 1 3 4a1 1 0 0 1 1-1h3.5a1 1 0 0 1 1 1c0 1.25.2 2.45.57 3.57a1 1 0 0 1-.25 1z"/></svg>
          978.555.0187
        </span>
      </address>
    </div>

    <ul class="contact-list">
      <li>
        <svg class="icon" viewBox="0 0 24 24" aria-hidden="true"><path d="M2 5h20v14H2z"/><path d="M2 5l10 7 10-7" fill="#fff"/></svg>
        frontdesk@halvercottortho.example
      </li>
      <li>
        <svg class="icon" viewBox="0 0 24 24" aria-hidden="true"><circle cx="12" cy="12" r="10"/></svg>
        www.halvercottortho.example
      </li>
    </ul>
  </section>
</body>
</html>
```